Cosmetic Clinic Looking For Sign Designs

We are looking for sign design ideas for the front of our building and a lawn sign for our cosmetic injection salon.
I have uploaded the front of our building for a mock up and size, lawn posts with size and a sign that uses the same dimensions.
We would like both signs to be black for the background.

Target Market(s)

Ages 18-75

Industry/Entity Type

Beauty

Requirements
Must have
• Services we offer:
• Cosmetic Injections
• Airbrush Spray Tanning
• Eyelash Growth Serum
• Skin Care Products & More
• Everything must be on a black background
• The lawn sign must have the address: 483 Fenwick and the building sign should have the phone number.
Should not have
• Nothing can light up (no LED)
• Both signs do not need the full address. Just 483 Fenwick and the phone number

```html
<!DOCTYPE html>
<html lang="en">
<head>
<meta charset="UTF-8">
<title>Velvet Dew Salon – Lawn Sign</title>
<link href="https://fonts.googleapis.com/css2?family=Roboto:wght@400;500;700&display=swap" rel="stylesheet">
<style>
  :root {
    --page-bg: #ecebe8;
    --sign-black: #1c1b21;
    --teal: #2bb4c8;
    --pink: #e2267c;
    --white: #ffffff;
    --soft-white: #e9e9ee;
  }
  * { margin: 0; padding: 0; box-sizing: border-box; }
  html, body {
    width: 900px;
    height: 1200px;
    overflow: hidden;
    background: var(--page-bg);
    font-family: "Roboto", Arial, sans-serif;
  }
  .canvas {
    position: relative;
    width: 900px;
    height: 1200px;
  }
  .lawn-sign {
    position: absolute;
    left: 40px;
    top: 290px;
    width: 820px;
    height: 620px;
    background: var(--sign-black);
    color: var(--white);
  }
  .brand-name {
    position: absolute;
    left: 0;
    right: 0;
    top: 212px;
    text-align: center;
    font-weight: 500;
    font-size: 56px;
    letter-spacing: 2px;
    line-height: 1;
    color: var(--teal);
    text-transform: uppercase;
  }
  .brand-sub {
    position: absolute;
    left: 0;
    right: 0;
    top: 282px;
    display: flex;
    justify-content: center;
    align-items: center;
    gap: 18px;
  }
  .brand-sub-text {
    font-weight: 400;
    font-size: 30px;
    letter-spacing: 3px;
    line-height: 1;
    color: var(--pink);
    text-transform: uppercase;
  }
  .brand-sub-rule {
    width: 96px;
    height: 3px;
    background: var(--pink);
  }
  .services {
    position: absolute;
    left: 0;
    right: 0;
    top: 352px;
    display: flex;
    justify-content: center;
  }
  .service-column {
    list-style: none;
    display: flex;
    flex-direction: column;
    gap: 30px;
    font-size: 22px;
    font-weight: 500;
    letter-spacing: 0.5px;
    text-transform: uppercase;
    color: var(--soft-white);
  }
  .service-column.left { text-align: right; padding-right: 24px; }
  .service-column.right { text-align: left; padding-left: 24px; }
  .service-divider {
    width: 3px;
    background: var(--pink);
  }
  .contact-rule {
    position: absolute;
    left: 50%;
    top: 478px;
    width: 370px;
    height: 3px;
    transform: translateX(-50%);
    background: var(--pink);
  }
  .address, .website {
    position: absolute;
    left: 0;
    right: 0;
    text-align: center;
    color: var(--teal);
    font-size: 32px;
    font-weight: 400;
  }
  .address { top: 502px; }
  .website { top: 556px; }
</style>
</head>
<body>
  <main class="canvas">
    <section class="lawn-sign">
      <h1 class="brand-name">Velvet Dew</h1>
      <div class="brand-sub">
        <span class="brand-sub-rule"></span>
        <span class="brand-sub-text">Salon</span>
        <span class="brand-sub-rule"></span>
      </div>
      <div class="services">
        <ul class="service-column left">
          <li>Cosmetic Injections</li>
          <li>Airbrush Spray Tanning</li>
        </ul>
        <div class="service-divider"></div>
        <ul class="service-column right">
          <li>Eyelash Growth Serum</li>
          <li>Skin Care Products &amp; More</li>
        </ul>
      </div>
      <div class="contact-rule"></div>
      <p class="address">483 Fenwick Street</p>
      <p class="website">www.velvetdewsalon.com</p>
    </section>
  </main>
</body>
</html>
```